R. Hallow & Hallow----- Truck repair shop, specialized in Heavy Duty truck Engines and maintance

First of all, I am looking for the perfect logo. In other words, I want a simple and easy to remember. Nowadays, diesel engines have accomplished much technological progress in emission reductions. As a manager, I understand that technology is an important tool in this industry. I don't want the usual logo that I see in shops such as trucks, pistons, wrenches. I want a logo and then a phrase saying specialists in Diesel Engines.

Target Market(s)

Truck Drivers, logistic companies, fleet

Contact Information for Business Card

Simple. Easy logo to remember.

Font styles to use
Serif

Colors

Designer to choose colors to be used in the design.

Requirements
Must have
• Business name
• Address 842 Marlow Street Brenton 08214 NJ
• Phone number
• email: rhallowandhallow@quennmail.com
Nice to have
• the Name should be " R. Hallow & Hallow " not R. Hallow AND Hallow
Should not have
• card should not have the usual logos of mechanic shops. e.g. cars, trucks, just a Logo

```html
<!DOCTYPE html>
<html lang="en">
<head>
<meta charset="utf-8">
<title>R. Hallow &amp; Hallow — Business Card</title>
<link rel="stylesheet" href="https://fonts.googleapis.com/css2?family=Crimson+Text:wght@400;600&display=swap">
<style>
  :root {
    --bg: #2b2b2d;
    --red: #d42237;
    --red-dark: #b81a2e;
    --ink: #3a3a3a;
    --ink-soft: #5a5a5a;
    --paper: #ffffff;
    --edge-grey: #4a4a4a;
  }
  * { box-sizing: border-box; margin: 0; padding: 0; }
  html, body { width: 1200px; height: 660px; overflow: hidden; }
  body {
    background: var(--bg);
    font-family: "Crimson Text", Georgia, serif;
    display: flex;
    align-items: center;
    justify-content: center;
    gap: 40px;
  }
  .card {
    position: relative;
    width: 540px;
    height: 309px;
    overflow: hidden;
    box-shadow: 0 14px 30px rgba(0,0,0,.45);
  }

  /* Front */
  .card-front {
    background: linear-gradient(135deg, var(--red-dark) 0%, var(--red) 55%, #dc3447 100%);
    color: var(--paper);
    display: flex;
    flex-direction: column;
    align-items: center;
    justify-content: center;
  }
  .front-mark {
    width: 62px; height: 62px;
    background: var(--paper);
    margin-bottom: 18px;
  }
  .front-name {
    font-size: 34px;
    font-weight: 600;
    letter-spacing: .5px;
    line-height: 1;
  }
  .front-tagline {
    margin-top: 6px;
    font-size: 12px;
    letter-spacing: 9px;
    text-transform: uppercase;
  }

  /* Back */
  .card-back { background: var(--paper); color: var(--ink); }
  .brand {
    position: absolute; left: 34px; top: 54px;
    display: flex; align-items: center; gap: 12px;
  }
  .brand-mark {
    width: 46px; height: 46px;
    background: var(--red);
  }
  .brand-name {
    font-size: 24px; font-weight: 600; color: var(--ink); line-height: 1;
  }
  .brand-tagline {
    margin-top: 3px;
    font-size: 10px; letter-spacing: 6px; color: var(--red);
    text-transform: uppercase;
  }
  .person {
    position: absolute; right: 34px; top: 50px;
    text-align: right;
  }
  .person-name { font-size: 17px; color: var(--ink-soft); line-height: 1; }
  .person-title { margin-top: 4px; font-size: 13px; color: var(--red); letter-spacing: 1px; }
  .divider {
    position: absolute; left: 34px; right: 34px; top: 122px;
    height: 1px; background: #555;
  }
  .contact-rule {
    position: absolute; left: 34px; width: 240px; top: 182px;
    height: 1px; background: #555;
  }
  .contacts {
    position: absolute; left: 34px; top: 192px;
    list-style: none; font-size: 14px; color: var(--ink); line-height: 1.35;
  }
  .contacts li { display: flex; align-items: center; gap: 8px; }
  .contacts svg { width: 11px; height: 11px; flex: none; }
  .address { margin-top: 4px; }
  .band {
    position: absolute; bottom: 0; height: 10px;
  }
  .band-grey { left: 0; width: 55%; background: var(--edge-grey); }
  .band-red { right: 0; width: 45%; background: var(--red); }
</style>
</head>
<body>

<section class="card card-front" aria-label="Business card front">
  <div class="front-mark"></div>
  <h1 class="front-name">R. Hallow &amp; Hallow</h1>
  <p class="front-tagline">Diesel Engines</p>
</section>

<section class="card card-back" aria-label="Business card back">
  <div class="brand">
    <div class="brand-mark"></div>
    <div>
      <h2 class="brand-name">R. Hallow &amp; Hallow</h2>
      <p class="brand-tagline">Diesel Engines</p>
    </div>
  </div>

  <div class="person">
    <p class="person-name">Your Name</p>
    <p class="person-title">Title</p>
  </div>

  <div class="divider"></div>
  <div class="contact-rule"></div>

  <ul class="contacts">
    <li>
      <svg viewBox="0 0 12 12" aria-hidden="true"><rect x="2.5" y="0.5" width="7" height="11" rx="1.2" fill="none" stroke="#d42237" stroke-width="1.4"/><rect x="4.5" y="9" width="3" height="1" fill="#d42237"/></svg>
      123.456.7890
    </li>
    <li>
      <svg viewBox="0 0 12 12" aria-hidden="true"><rect x="0.5" y="2" width="11" height="8" fill="#d42237"/><path d="M1 2.5 L6 7 L11 2.5" fill="none" stroke="#fff" stroke-width="1.2"/></svg>
      rhallowandhallow@quennmail.com
    </li>
    <li class="address">Address 842 Marlow Street</li>
    <li>Brenton 08214 NJ</li>
  </ul>

  <div class="band band-grey"></div>
  <div class="band band-red"></div>
</section>

</body>
</html>
```